Expedite Project: Personal Assessment Document
Document of your "Personal Assessment"
Expedite Project: Personal Assessment Document - Consulting
Creative Brief
Consulting
For Men Only. Professional Personal ( No cartoons )
Logo design files: https://www.filebinder.example/s/k83pq2vn7tz4rs9/Files.zip There needs to be ample room under each question for their answers. I want the logo included and I want my picture on there at the end with a thank you message under my picture. I will forward the short message to the winner of the project. (I want this info on the document) Harbor Lantern Path www.harborlanternpath.example dwight@harborlanternpath.example 555-384-9162
JBrennig917 JBrennig917
If any of you have a real picture of a mountain to place in the background either with or without a person please submit. Not sure which design I want yet I could go with the mountain and could go without it. Turn in designs quick Im about to make a selection. Send in all your designs please.
The theme to my website will involve mountain views, hence, Harbor Lantern Path. I have a number of other snow covered mountain themes. It does not have to be but this is a lot of the themes. Please don't feel it has be be mountain themes, but if you want to include at least one of your designs that way that would be fine.

```html
<!DOCTYPE html>
<html lang="en">
<head>
<meta charset="utf-8">
<title>Personal Assessment – Harbor Lantern Path</title>
<link rel="stylesheet" href="https://fonts.googleapis.com/css2?family=Open+Sans:ital,wght@0,400;0,600;0,700;0,800;1,400;1,600&display=swap">
<style>
:root{
  --stage:#4f4f4f;
  --paper:#ffffff;
  --navy:#151a5c;
  --navy-deep:#0f1247;
  --glow:#3b74c6;
  --accent:#2d68bd;
  --ink:#2e2e2e;
  --hint:#a3a3a3;
  --rule:#5a5a5a;
  --panel:#d9d9d9;
  --strip:#c9c9c9;
  --photo:#8e8e8e;
  --photo-text:#b3b3b3;
}
*{box-sizing:border-box;margin:0;padding:0}
html,body{width:1200px;height:714px;overflow:hidden}
body{background:var(--stage);font-family:"Open Sans",Arial,sans-serif;color:var(--ink);position:relative}
.page{position:absolute;top:4px;width:545px;height:705px;background:var(--paper);overflow:hidden}
.page--front{left:31px}
.page--back{left:625px}
.band{position:absolute;left:0;width:100%;background:linear-gradient(90deg,var(--navy-deep),var(--navy) 28%,var(--glow) 50%,var(--navy) 72%,var(--navy-deep))}
.band--top{top:0;height:33px;box-shadow:0 3px 0 #fff,0 5px 0 var(--navy)}
.band--bottom{bottom:0;height:19px;box-shadow:0 -3px 0 #fff,0 -5px 0 var(--navy)}
.brand{position:absolute;left:12px;top:56px;width:270px;text-align:center}
.brand__mark{display:block;width:88px;height:88px;margin:0 auto 10px;border-radius:50%;background:var(--navy)}
.brand__name{font-weight:800;font-size:23px;line-height:27px;color:var(--navy);text-transform:uppercase;white-space:nowrap}
.doc-title{position:absolute;right:24px;top:82px;font-size:20px;font-weight:700;color:var(--accent)}
.contact{position:absolute;right:24px;top:156px;text-align:right;font-size:12.5px;line-height:16px;color:#222}
.rule{position:absolute;left:15px;right:15px;height:1px;background:var(--rule)}
.sec{position:absolute;left:24px;font-size:15px;font-weight:700;color:var(--accent);line-height:20px}
.yn{position:absolute;left:463px;font-size:14px;line-height:20px;color:#222;display:flex;gap:11px}
.q{position:absolute;left:43px;width:415px;font-size:9.6px;letter-spacing:-0.2px;line-height:13px;color:var(--ink)}
.q--line{white-space:nowrap}
.q::before{content:"•";position:absolute;left:-8px}
.hint{position:absolute;left:43px;font-size:9.5px;font-style:italic;color:var(--hint);line-height:13px}
.pick{position:absolute;left:470px;display:flex;gap:21px}
.pick i{display:block;width:10px;height:10px;border:1px solid #555;border-radius:50%}
.page--back .yn{left:464px}
.closing{position:absolute;left:0;top:496px;width:100%;height:162px;background:var(--panel)}
.portrait{position:absolute;left:24px;top:18px;width:131px;height:126px;border-radius:8px;background:var(--photo);display:flex;align-items:center;justify-content:center;text-align:center;font-size:21px;font-weight:700;line-height:31px;color:var(--photo-text)}
.message{position:absolute;left:171px;top:26px;width:354px}
.message h3{font-size:14.5px;font-weight:400;font-style:italic;color:var(--navy);line-height:20px}
.message p{font-size:9.6px;font-style:italic;line-height:13px;color:#333}
.contact-strip{position:absolute;left:0;top:658px;width:100%;height:26px;background:var(--strip);display:flex;align-items:center;justify-content:space-between;padding:0 14px 0 20px;font-size:10.5px;color:var(--navy);white-space:nowrap}
.contact-strip span{display:flex;align-items:center;gap:4px}
.contact-strip svg{width:11px;height:11px;flex:none}
</style>
</head>
<body>

<section class="page page--front">
  <div class="band band--top"></div>

  <div class="brand">
    <span class="brand__mark"></span>
    <div class="brand__name">Harbor Lantern<br>Path</div>
  </div>
  <h1 class="doc-title">Personal Assessment</h1>
  <div class="contact">
    www.harborlanternpath.example<br>
    dwight@harborlanternpath.example<br>
    555-384-9162
  </div>

  <div class="rule" style="top:233px"></div>

  <h2 class="sec" style="top:248px">Identity</h2>
  <div class="yn" style="top:248px"><span>Yes</span><span>No</span></div>
  <p class="q" style="top:272px">Reflect on the roles by which you define yourself – or allow yourself to be defined (spouse, parent, boss, etc.)</p>
  <div class="pick" style="top:274px"><i></i><i></i></div>
  <p class="q q--line" style="top:303px">Do you define yourself by your work, such as “realtor” or “nurse”?</p>
  <div class="pick" style="top:305px"><i></i><i></i></div>
  <p class="q q--line" style="top:321px">Do you define yourself by a relationship, such as “wife” or “son”?</p>
  <div class="pick" style="top:323px"><i></i><i></i></div>
  <p class="q q--line" style="top:339px">What is your core identity that transcends all roles and relationships?</p>
  <p class="hint" style="top:356px">Type Your Answers Here</p>
  <p class="q q--line" style="top:390px">Does your sense of self feel internally consistent despite varying external contexts?</p>
  <div class="pick" style="top:392px"><i></i><i></i></div>
  <p class="q q--line" style="top:408px">Who do you say you are?</p>
  <p class="hint" style="top:424px">Type Your Answers Here</p>

  <div class="rule" style="top:460px"></div>

  <h2 class="sec" style="top:468px">Ideals</h2>
  <div class="yn" style="top:468px"><span>Yes</span><span>No</span></div>
  <p class="q q--line" style="top:492px">Do you have a clear internal vision of whom and what you want to be?</p>
  <div class="pick" style="top:494px"><i></i><i></i></div>
  <p class="q q--line" style="top:510px">Are you living up to your own ideals?</p>
  <div class="pick" style="top:512px"><i></i><i></i></div>
  <p class="q q--line" style="top:528px">Have you realized your potential?</p>
  <div class="pick" style="top:530px"><i></i><i></i></div>

  <div class="rule" style="top:551px"></div>

  <h2 class="sec" style="top:558px">Needs</h2>
  <div class="yn" style="top:558px"><span>Yes</span><span>No</span></div>
  <p class="q q--line" style="top:582px">Do your basic needs and ideals align with your goals?</p>
  <div class="pick" style="top:584px"><i></i><i></i></div>
  <p class="q q--line" style="top:600px">Do you need to become more of who you really are?</p>
  <div class="pick" style="top:602px"><i></i><i></i></div>
  <p class="q" style="top:618px">Do you deny your wants or needs to avoid conflict, to please others, or to take care of others?</p>
  <div class="pick" style="top:620px"><i></i><i></i></div>

  <div class="band band--bottom"></div>
</section>

<section class="page page--back">
  <div class="band band--top"></div>

  <h2 class="sec" style="top:49px">Relationship</h2>
  <div class="yn" style="top:49px"><span>Yes</span><span>No</span></div>
  <p class="q" style="top:73px">Who are you (or whom do you become) in an important relationship, such as with a spouse?</p>
  <p class="hint" style="top:100px">Type Your Answers Here</p>
  <p class="q q--line" style="top:136px">In a relationship, is your personal growth facilitated, stymied, or ignored?</p>
  <div class="pick" style="top:138px"><i></i><i></i></div>
  <p class="q" style="top:154px">Do you lose your individuality by finding yourself in your partner or spouse’s identity? Do you feel “less than” rather than “equal to”?</p>
  <div class="pick" style="top:156px"><i></i><i></i></div>
  <p class="q q--line" style="top:185px">What goals have you accomplished in your life?</p>
  <p class="hint" style="top:200px">Type Your Answers Here</p>
  <p class="q q--line" style="top:235px">What goals have yet to be achieved?</p>
  <p class="hint" style="top:250px">Type Your Answers Here</p>

  <div class="rule" style="top:295px"></div>

  <h2 class="sec" style="top:302px">Career</h2>
  <div class="yn" style="top:302px"><span>Yes</span><span>No</span></div>
  <p class="q q--line" style="top:325px">Who are you in your career?</p>
  <p class="hint" style="top:338px">Type Your Answers Here</p>
  <p class="q q--line" style="top:375px">Do you define yourself by your job description?</p>
  <p class="hint" style="top:390px">Type Your Answers Here</p>
  <p class="q q--line" style="top:426px">Are you reaching your full potential at work?</p>
  <div class="pick" style="top:428px"><i></i><i></i></div>
  <p class="q" style="top:444px">Do you create a self-definition that facilitates growth, with definite goals, a specific and evolving life and career plan, and measurable success?</p>
  <div class="pick" style="top:446px"><i></i><i></i></div>

  <div class="closing">
    <div class="portrait" role="img" aria-label="Portrait photo of the consultant">YOUR<br>PICTURE</div>
    <div class="message">
      <h3>Your Message Here</h3>
      <p>Lorem ipsum dolor sit amet, consectetur adipiscing elit. Quisque sem tortor, ultrices ac congue id, volutpat sed magna. In et lorem vel dolor rhoncus accumsan. Proin laoreet odio ac dolor placerat luctus fringilla mi commodo. Vivamus et nibh viverra diam pulvinar interdum. Sed sit amet mi diam, sed elementum arcu. Etiam nisl erat, egestas vitae posuere cursus, imperdiet ac lorem. Morbi vitae quam justo, ut convallis orci. Donec pulvinar semper lectus, et aliquam ligula tempus quis. Mauris id augue est. Morbi ante velit, bibendum nec dignissim eget, vulputate et nisl.</p>
    </div>
  </div>

  <div class="contact-strip">
    <span><svg viewBox="0 0 12 12" fill="none" stroke="#555" stroke-width="1"><circle cx="6" cy="6" r="5"/><ellipse cx="6" cy="6" rx="2.2" ry="5"/><line x1="1" y1="6" x2="11" y2="6"/></svg>www.harborlanternpath.example</span>
    <span><svg viewBox="0 0 12 12" fill="#555"><rect x="0.5" y="2.5" width="11" height="7"/><path d="M0.5 2.5 6 7 11.5 2.5" fill="none" stroke="#ddd" stroke-width="1"/></svg>dwight@harborlanternpath.example</span>
    <span><svg viewBox="0 0 12 12" fill="#555"><path d="M2.5 1 4.5 1 5.2 3.8 4 4.8C4.7 6.4 5.6 7.3 7.2 8L8.2 6.8 11 7.5 11 9.5C11 10.3 10.3 11 9.5 11 5 11 1 7 1 2.5 1 1.7 1.7 1 2.5 1Z"/></svg>555-384-9162</span>
  </div>

  <div class="band band--bottom"></div>
</section>

</body>
</html>
```